30th Anniversary Poster

Need a 2ft (Wide) X 3ft (Tall) Poster design for a 30th anniversary party that will be used in .  Need the get the logo to be the theme colors (gold).  Overall theme is elegance with gold and black being the main colors.  The background should be black.  Silver can be used as an accent color.  I need the sign to say Welcome and 30th Anniversary.  I need all text to be editable and fonts easily available.
A feel similar to images in this search is pretty close.
https://www.brivolsearch.example/find?tk=9b2e71c04d8a5f36&ref=7QXPLMZ_wnTR441TR441&sid=KQPWRTzNmv8LdHysXaPq2GbTc3RrxW:2841099670862&q=gala+event+poster&mode=2&flt=ZRTQmB1Bb5tjXe43Ry6qFxSkVe9cPKgmzCSTTT6OS4wLVQ8yXt7ZdHyUg39F7Nalr4MkiDuS42Z9kOnPyrk1jfnd0Bp8RwhSbbCqXfe7YdWkpPmX1zYXMS6W2olZPTbejwdwlW27yNbCepq98SaKnGcdJvHpE1Ddb2Y4UbrTBkS6SVtXdTDVBq1XCUc7-1DVXDpXpV-Tfk8Xk_MwspEsTvLvWAqp9-IBcqmUh_NGXYB&ax=Y&ib=3&vx=3bqVLxj3ttrkBzYkNeGqUJQV&bw=1728&bh=840&pr=2

```html
<!DOCTYPE html>
<html lang="en">
<head>
<meta charset="utf-8">
<title>30th Anniversary Party – Welcome Poster</title>
<link rel="stylesheet" href="https://fonts.googleapis.com/css2?family=Bodoni+Moda:wght@400;500&family=Great+Vibes&family=Oswald:wght@200&family=Poppins:wght@300;400;500;700&family=Josefin+Sans:wght@400&display=swap">
<style>
  :root{
    --page:#c4c4c4;
    --black:#060606;
    --ink:#0d0d0d;
    --gold:#c9954f;
    --gold-light:#e2b878;
    --gold-deep:#9a6a2e;
    --silver:#e4e4e4;
    --silver-dark:#8c8c8c;
    --white:#ffffff;
  }
  *{margin:0;padding:0;box-sizing:border-box}
  html,body{width:1200px;height:888px;overflow:hidden;background:var(--page)}
  .poster{
    position:absolute;left:312px;top:12px;width:576px;height:864px;overflow:hidden;
    background:
      radial-gradient(circle at 30% 8%, rgba(201,149,79,.16), transparent 22%),
      radial-gradient(circle at 60% 88%, rgba(201,149,79,.14), transparent 24%),
      linear-gradient(160deg,#141414 0%,var(--black) 55%,#111 100%);
  }
  .brand{position:absolute;left:0;width:288px;top:96px;display:flex;align-items:center;justify-content:center;gap:8px}
  .brand__dot{width:18px;height:18px;border-radius:50%;background:var(--gold)}
  .brand__name{font:500 13px/1 'Poppins',sans-serif;color:var(--silver);letter-spacing:.5px}
  .title-number{
    position:absolute;left:52px;top:176px;
    font:400 226px/1 'Bodoni Moda',serif;letter-spacing:-6px;
    background:linear-gradient(100deg,#7e7e7e 0%,#f4f4f4 30%,#9a9a9a 48%,#ffffff 62%,#8a8a8a 100%);
    -webkit-background-clip:text;background-clip:text;color:transparent;
  }
  .title-number sup{font-size:52px;vertical-align:top;position:relative;top:18px;letter-spacing:0;margin-left:4px}
  .title-script{position:absolute;left:56px;top:384px;width:280px;text-align:center;font:400 56px/1 'Great Vibes',cursive;color:var(--gold)}
  .title-main{position:absolute;left:54px;top:432px;font:200 82px/1 'Oswald',sans-serif;letter-spacing:17px;color:var(--white)}
  .rules{position:absolute;left:56px;top:553px;width:126px}
  .rules span{display:block;height:1px;background:var(--gold);margin-bottom:7px;opacity:.85}
  .date{position:absolute;left:56px;top:626px;display:flex;align-items:center;gap:12px}
  .date__day{font:700 66px/1 'Poppins',sans-serif;color:transparent;-webkit-text-stroke:2px var(--silver);letter-spacing:-2px}
  .date__month{font:700 27px/1 'Poppins',sans-serif;color:var(--white);display:block}
  .date__year{font:300 29px/1 'Poppins',sans-serif;color:var(--gold);letter-spacing:5px;display:block;margin-top:4px}
  .website{position:absolute;left:56px;top:798px;font:400 14px/1 'Poppins',sans-serif;color:var(--white);letter-spacing:3.2px}
  .welcome-band{position:absolute;left:380px;top:0;width:156px;height:826px}
  .welcome-word{
    position:absolute;left:412px;top:66px;writing-mode:vertical-rl;
    font:400 74px/1 'Josefin Sans',sans-serif;letter-spacing:7px;color:var(--ink);
  }
  .welcome-to{position:absolute;left:428px;top:630px;transform:rotate(90deg);font:400 46px/1 'Great Vibes',cursive;color:var(--white)}
</style>
</head>
<body>
<main class="poster">
  <div class="brand"><span class="brand__dot"></span><span class="brand__name">HALVERN SYSTEMS</span></div>

  <h1 class="title-number">30<sup>th</sup></h1>
  <p class="title-script">Anniversary</p>
  <p class="title-main">PARTY</p>

  <div class="rules"><span></span><span></span><span></span><span></span></div>

  <div class="date">
    <span class="date__day">24</span>
    <span><span class="date__month">NOVEMBER</span><span class="date__year">2024</span></span>
  </div>

  <p class="website">www.halvernsystems.example</p>

  <svg class="welcome-band" viewBox="0 0 156 826" preserveAspectRatio="none" aria-hidden="true">
    <defs>
      <linearGradient id="goldBand" x1="0" y1="0" x2="1" y2="1">
        <stop offset="0" stop-color="#a8773a"/>
        <stop offset=".35" stop-color="#e2b878"/>
        <stop offset=".6" stop-color="#c9954f"/>
        <stop offset="1" stop-color="#8f622a"/>
      </linearGradient>
    </defs>
    <path fill="url(#goldBand)" d="M10 0 L148 0 L142 40 L150 90 L144 150 L152 220 L145 300 L151 380 L144 450 L150 520 L143 600 L149 660 L140 720 L146 770 L132 800 L118 826 L100 812 L86 826 L70 808 L52 818 L40 790 L26 770 L20 720 L12 660 L18 600 L8 520 L14 450 L6 380 L13 300 L5 220 L12 150 L4 90 L11 40 Z"/>
  </svg>
  <p class="welcome-word">WELCOME</p>
  <p class="welcome-to">to</p>
</main>
</body>
</html>
```